Business Card design for law firm = Juriskite Australia

We are seeking a new design for our business cards.
We are keeping our logo, which is attached.
We need space for
Name
Title
Address is , which is
Level 14
82 Penhallow Street
Sydney NSW 2000
Phone :
Mobile :
Fax :
Email :
DX :
website www.juriskite.com.au

Industry/Entity Type

Law Firm / Banking and Finance

Contact Information for Business Card

We are seeking a new design for our business cards. We are keeping our logo. We need space for Name Title Address is Level 14 82 Penhallow Street Sydney NSW 2000 Phone Mobile Fax Email DX website www.juriskite.com.au

Colors
0054AA
0677BA
7BADD7
CADEEF
E8F1F8

Requirements
Must have
• see our website for general feel www.juriskite.com.au

```html
<!DOCTYPE html>
<html lang="en">
<head>
<meta charset="utf-8">
<title>Juriskite Australia – Business Card</title>
<link href="https://fonts.googleapis.com/css2?family=Open+Sans:wght@400;600&display=swap" rel="stylesheet">
<style>
  :root {
    --navy: #0054AA;
    --cyan: #0677BA;
    --sky: #7BADD7;
    --mist: #CADEEF;
    --ice: #E8F1F8;
    --ink: #4a4f57;
    --stage: #3b342f;
    --paper: #ffffff;
  }
  * { box-sizing: border-box; margin: 0; padding: 0; }
  html, body {
    width: 1200px; height: 913px; overflow: hidden;
    background: var(--stage);
    font-family: "Open Sans", Arial, sans-serif;
  }
  .sheet {
    width: 1200px; height: 913px;
    display: flex; flex-direction: column; align-items: center; justify-content: center;
    gap: 40px;
  }
  .card {
    width: 700px; height: 400px;
    position: relative;
    box-shadow: 0 14px 30px rgba(0,0,0,0.45);
  }
  .card--front {
    background: linear-gradient(100deg, #0a8cc6 0%, #2a9ccc 25%, #6aa3cb 45%, #4f86c0 72%, #2c6cb4 100%);
    display: flex; align-items: center; justify-content: center;
  }
  .brand__name {
    font-weight: 400; font-size: 52px; letter-spacing: 1px; line-height: 1;
    color: var(--paper);
  }
  .card--back { background: var(--paper); }
  .card--back .brand {
    position: absolute; left: 48px; top: 128px;
  }
  .card--back .brand__name { color: var(--navy); font-size: 48px; }
  .contact {
    position: absolute; right: 40px; top: 60px;
    font-size: 14px; line-height: 1.45; color: var(--ink);
  }
  .contact__label { color: var(--navy); font-weight: 600; display: inline-block; width: 22px; }
  .contact__group + .contact__group { margin-top: 12px; }
  .contact__dx { color: var(--navy); }
  .person {
    position: absolute; left: 48px; bottom: 48px;
  }
  .person__name { color: var(--navy); font-weight: 600; font-size: 22px; }
  .person__title { color: var(--ink); font-size: 16px; }
</style>
</head>
<body>
  <main class="sheet">
    <section class="card card--front" aria-label="Card front">
      <div class="brand">
        <span class="brand__name">Juriskite</span>
      </div>
    </section>

    <section class="card card--back" aria-label="Card back">
      <div class="brand">
        <span class="brand__name">Juriskite</span>
      </div>

      <div class="contact">
        <div class="contact__group">
          <div><span class="contact__label">M.</span>0412 604 385</div>
          <div><span class="contact__label">T.</span>02 9460 3318</div>
          <div><span class="contact__label">F.</span>02 9460 3319</div>
        </div>
        <div class="contact__group">
          <div><span class="contact__label">E.</span>enquiries@juriskite.com.au</div>
          <div><span class="contact__label">W.</span>www.juriskite.com.au</div>
        </div>
        <div class="contact__group">
          <div>Level 14, 82 Penhallow Street</div>
          <div>Sydney NSW 2000</div>
          <div class="contact__dx">DX 318 Sydney</div>
        </div>
      </div>

      <div class="person">
        <div class="person__name">Sam Whitford</div>
        <div class="person__title">Managing Director</div>
      </div>
    </section>
  </main>
</body>
</html>
```